Young, funky marketing collateral and other stuff
Exciting and innovative ideas welcomed
We are thrilled with the designs that have come in and are now spoilt for choice as they are all individually very good. We appreciate the trouble you have gone to in response to our direct feedback as we 'fine tune' our ideas. Thanks designers, you are all great.
A big thank you also to Owen in Support who has helped to smooth the way between us and the designers when we have run into difficulty conveying some of our ideas.
Have already recommended Tallowspan to others
Regards
RTolley
Fernwick logo
#14: the way that the fernwick logo colours have been made neutral is very good and perfectly acceptable to us.
A general reminder; fernwick logo only on biz card, folder, letterhead and signature. Not on other things.
Address Label:
#13 has the right idea for the address label, however we would like it to be landscape design rather than portrait
Yard signs: it would be good to have the branding colours 'frame' the signs in some way too thanks. Thanks for your great efforts.
Hi Designers
On the yard signs, please include as part of the branding template:
www.kvtp.co.nz
Thanks
Clarification on Registry. Please use the following 'Open for Inspection Registry' not 'Open House Registry'. Thanks.
Also, the Registry does not require fernwick logo.
Brightnook, thanks for your ideas. #4 is attractive, we prefer the way you have presented the company address in the letterhead, by contrast in #3 the company address in footer looks a bit staggered and not so smart. The logo reflection on the #4 folder is also very appealing.
#5 Thank you for your new design.
The address label; please make the dot dot lines in the receiver's address longer and more central. We will be handwriting the receiver's address on the dot dot line and it needs to have enough space to do this and so that a courier or post office can read the address and deliver the package easily.
Thanks for the new designs. I can see that trying to incorporate the 2nd logo (fernwick property) is simply going to cause confusion however we do need somehow to represent the second company. Instead of using logo, please just use company name and designation which is 'Fernwick Property Ltd, Licensed Agent (PLNB) 2008. Please include this on the business card, folder, letterhead, and signature. It would be suitable to have it, for instance, in the bottom line of the footer, the two company names as bullet points.
@DW - please check your private message on top right corner after clicking messages once you log in. Thanks
A big thanks to pixvellor for starting of the process with neat designs #1 and #2.
My brief may not have been totally clear so here are a couple more thoughts:
The mailing label: There needs to be a space (........... line) after 'company/name etc so that the sender can hand write the details in. For example:
Company/Name ...........................................
Address .................................................
.........................................................City ....................................................
Phone ...................................................
Attention ...............................................
Please also note my comment at start of brief about also including Fernwick property details on some of the collateral. If it's going to look too crowded, just use the fernwick logo.
On the 'inspect today' sign, the 'inspect today' plus arrow are major components, the branding is minor. This sign will be placed at intersections directing buyers to a home, so the size of the arrow is important.
Thanks everyone and we look forward to seeing your ideas.

```html
<!DOCTYPE html>
<html lang="en">
<head>
<meta charset="utf-8">
<title>Kestrel Vale – Collateral Set</title>
<link href="https://fonts.googleapis.com/css2?family=Montserrat:wght@400;600;700&display=swap" rel="stylesheet">
<style>
  :root {
    --blue: #1e9ad6;
    --blue-dark: #0b6fae;
    --blue-light: #8fd0f2;
    --blue-pale: #dff1fb;
    --ink: #3b4a57;
    --grey: #9aa6b0;
    --paper: #ffffff;
    --board: #ffffff;
    --edge: #d5dde3;
  }
  * { box-sizing: border-box; margin: 0; padding: 0; }
  html, body { width: 1200px; height: 365px; overflow: hidden; background: var(--board); }
  body { font-family: "Montserrat", Arial, sans-serif; color: var(--ink); position: relative; }

  .piece { position: absolute; background: var(--paper); border: 1px solid var(--edge); overflow: hidden; }
  .piece svg.wave { position: absolute; left: 0; width: 100%; }
  .item-label { position: absolute; font-size: 6px; color: var(--grey); font-weight: 600; }

  .brand { display: flex; align-items: center; gap: 4px; }
  .brand .mark { background: var(--blue); flex: none; }
  .brand .name { color: var(--blue); font-weight: 700; letter-spacing: .04em; white-space: nowrap; }

  /* Pocket folder */
  .folder-back { left: 12px; top: 48px; width: 222px; height: 268px; }
  .folder-front { left: 234px; top: 48px; width: 222px; height: 268px; }
  .folder-back .logo-tile { position: absolute; left: 56px; top: 22px; width: 110px; height: 72px; background: var(--blue-pale); display: flex; align-items: center; justify-content: center; }
  .folder-back .logo-tile .mark { width: 16px; height: 16px; }
  .folder-back .logo-tile .name { font-size: 11px; }
  .folder-back .agent { position: absolute; left: 0; width: 100%; top: 100px; text-align: center; font-size: 5px; line-height: 1.5; color: var(--ink); }
  .folder-back .partner { position: absolute; left: 0; width: 100%; top: 126px; display: flex; justify-content: center; }
  .folder-back .partner span { font-size: 6px; font-weight: 600; color: var(--ink); }
  .folder-front .web { position: absolute; left: 0; width: 100%; top: 200px; text-align: center; font-size: 5px; color: var(--ink); }
  .pocket { position: absolute; left: 12px; top: 316px; width: 444px; height: 40px; }

  /* Letterhead */
  .letterhead { left: 492px; top: 53px; width: 96px; height: 188px; }
  .letterhead .brand { position: absolute; left: 8px; top: 22px; }
  .letterhead .mark { width: 7px; height: 7px; }
  .letterhead .name { font-size: 6px; }
  .letterhead .foot { position: absolute; left: 0; width: 100%; bottom: 6px; text-align: center; font-size: 3px; color: var(--ink); }

  /* Business cards */
  .card { width: 89px; height: 52px; }
  .card-front { left: 595px; top: 60px; }
  .card-back { left: 595px; top: 130px; }
  .card-alt { left: 595px; top: 190px; height: 38px; }
  .card .brand { position: absolute; left: 6px; top: 12px; }
  .card .mark { width: 5px; height: 5px; }
  .card .name { font-size: 4.5px; }
  .card .details { position: absolute; left: 6px; top: 24px; font-size: 3.5px; line-height: 1.5; }
  .card-back .brand { left: 20px; top: 20px; }
  .card-back .mark { width: 7px; height: 7px; }
  .card-back .name { font-size: 6px; }

  /* Address label */
  .label { left: 492px; top: 276px; width: 48px; height: 46px; }

  /* Signature */
  .signature { left: 595px; top: 276px; width: 100px; height: 26px; }
  .signature .brand { position: absolute; left: 4px; top: 9px; }
  .signature .mark { width: 5px; height: 5px; }
  .signature .name { font-size: 4px; }
  .signature .details { position: absolute; left: 52px; top: 7px; font-size: 3.5px; line-height: 1.5; }

  /* Sign */
  .sign { left: 700px; top: 48px; width: 492px; height: 306px; }
  .sign .photo { position: absolute; left: 0; top: 80px; width: 100%; height: 170px; background: linear-gradient(180deg, #a9cfe6 0%, #dfe6ea 40%, #c9c2b4 70%, #6f8a57 100%); }
  .sign .tagline { position: absolute; right: 14px; top: 10px; color: var(--paper); font-size: 14px; font-weight: 400; }
  .sign .brand { position: absolute; left: 16px; top: 70px; gap: 8px; }
  .sign .mark { width: 30px; height: 30px; }
  .sign .name { font-size: 24px; }
  .sign .web { position: absolute; left: 18px; bottom: 12px; color: var(--paper); font-size: 13px; }
</style>
</head>
<body>

  <span class="item-label" style="left:12px;top:38px">Pocket Folder</span>
  <span class="item-label" style="left:492px;top:43px">Letter Head</span>
  <span class="item-label" style="left:640px;top:52px">Biz Card Front</span>
  <span class="item-label" style="left:640px;top:122px">Biz Card Back</span>
  <span class="item-label" style="left:595px;top:268px">Signature</span>
  <span class="item-label" style="left:700px;top:38px">Sign</span>

  <!-- Pocket folder -->
  <div class="piece folder-back">
    <div class="logo-tile brand"><span class="mark"></span><span class="name">KESTREL VALE</span></div>
    <p class="agent">Licensed Sales Agent<br>Fernwick Property Ltd, Licensed Agent (PLNB) 2008</p>
    <div class="partner"><span>Fernwick Property Ltd</span></div>
    <svg class="wave" style="bottom:0;height:70px" viewBox="0 0 222 70" preserveAspectRatio="none">
      <path d="M0 30 C60 60 140 10 222 40 L222 70 L0 70Z" fill="var(--blue-light)"/>
      <path d="M0 45 C70 70 150 25 222 55 L222 70 L0 70Z" fill="var(--blue)"/>
    </svg>
  </div>
  <div class="piece folder-front">
    <p class="web">www.kvtp.co.nz</p>
    <svg class="wave" style="bottom:0;height:60px" viewBox="0 0 222 60" preserveAspectRatio="none">
      <path d="M0 25 C80 55 150 5 222 30 L222 60 L0 60Z" fill="var(--blue-light)"/>
      <path d="M0 38 C80 62 160 20 222 44 L222 60 L0 60Z" fill="var(--blue)"/>
    </svg>
  </div>
  <svg class="pocket" viewBox="0 0 444 40" preserveAspectRatio="none">
    <path d="M0 0 L222 0 L222 30 Q190 40 150 34 L30 34 Q8 30 0 12Z" fill="var(--blue)" stroke="var(--edge)"/>
    <path d="M222 0 L444 0 L444 12 Q436 30 414 34 L294 34 Q254 40 222 30Z" fill="var(--blue-light)" stroke="var(--edge)"/>
  </svg>

  <!-- Letterhead -->
  <div class="piece letterhead">
    <svg class="wave" style="top:0;height:20px" viewBox="0 0 96 20" preserveAspectRatio="none">
      <path d="M0 0 L96 0 L96 8 C60 20 30 4 0 14Z" fill="var(--blue)"/>
    </svg>
    <div class="brand"><span class="mark"></span><span class="name">KESTREL VALE</span></div>
    <p class="foot">Fernwick Property Ltd · www.kvtp.co.nz</p>
    <svg class="wave" style="bottom:0;height:14px" viewBox="0 0 96 14" preserveAspectRatio="none">
      <path d="M0 6 C30 14 60 0 96 8 L96 14 L0 14Z" fill="var(--blue-light)"/>
    </svg>
  </div>

  <!-- Business cards -->
  <div class="piece card card-front">
    <svg class="wave" style="top:0;height:10px" viewBox="0 0 89 10" preserveAspectRatio="none">
      <path d="M0 0 L89 0 L89 4 C60 10 30 2 0 7Z" fill="var(--blue)"/>
    </svg>
    <div class="brand"><span class="mark"></span><span class="name">KESTREL VALE</span></div>
    <p class="details">Agent Name<br>Licensed Sales Agent<br>www.kvtp.co.nz</p>
  </div>
  <div class="piece card card-back">
    <svg class="wave" style="bottom:0;height:14px" viewBox="0 0 89 14" preserveAspectRatio="none">
      <path d="M0 4 C30 14 60 0 89 6 L89 14 L0 14Z" fill="var(--blue)"/>
    </svg>
    <div class="brand"><span class="mark"></span><span class="name">KESTREL VALE</span></div>
  </div>
  <div class="piece card card-alt">
    <svg class="wave" style="top:0;height:10px" viewBox="0 0 89 10" preserveAspectRatio="none">
      <path d="M0 0 L89 0 L89 4 C60 10 30 2 0 7Z" fill="var(--blue)"/>
    </svg>
    <div class="brand"><span class="mark"></span><span class="name">KESTREL VALE</span></div>
  </div>

  <!-- Address label -->
  <div class="piece label">
    <svg class="wave" style="top:0;height:12px" viewBox="0 0 48 12" preserveAspectRatio="none">
      <path d="M0 0 L48 0 L48 5 C30 12 15 3 0 8Z" fill="var(--blue)"/>
    </svg>
    <svg class="wave" style="bottom:0;height:10px" viewBox="0 0 48 10" preserveAspectRatio="none">
      <path d="M0 4 C15 10 30 0 48 5 L48 10 L0 10Z" fill="var(--blue-light)"/>
    </svg>
  </div>

  <!-- Email signature -->
  <div class="piece signature">
    <svg class="wave" style="bottom:0;height:6px" viewBox="0 0 100 6" preserveAspectRatio="none">
      <path d="M0 2 C30 6 70 0 100 3 L100 6 L0 6Z" fill="var(--blue)"/>
    </svg>
    <div class="brand"><span class="mark"></span><span class="name">KESTREL VALE</span></div>
    <p class="details">Agent Name<br>Sales Agent<br>Fernwick Property Ltd</p>
  </div>

  <!-- Sign -->
  <div class="piece sign">
    <div class="photo" role="img" aria-label="Photograph of a large modern home with a pool and garden"></div>
    <svg class="wave" style="top:0;height:120px" viewBox="0 0 492 120" preserveAspectRatio="none">
      <path d="M0 0 L492 0 L492 60 C380 110 200 40 0 110Z" fill="var(--paper)"/>
      <path d="M0 0 L492 0 L492 40 C360 80 220 20 0 60Z" fill="var(--blue-light)"/>
      <path d="M60 0 L492 0 L492 30 C380 60 250 10 60 40Z" fill="var(--blue)"/>
    </svg>
    <p class="tagline">Save thousands in commission</p>
    <div class="brand"><span class="mark"></span><span class="name">KESTREL VALE</span></div>
    <svg class="wave" style="bottom:0;height:80px" viewBox="0 0 492 80" preserveAspectRatio="none">
      <path d="M0 20 C150 60 320 0 492 30 L492 80 L0 80Z" fill="var(--blue-light)"/>
      <path d="M0 35 C160 75 330 20 492 45 L492 80 L0 80Z" fill="var(--blue)"/>
    </svg>
    <p class="web">www.kvtp.co.nz</p>
  </div>

</body>
</html>
```